Harrow Collective
Chartered accountants & business advisors company seeks logo & business card design refresh - Financial Services
Simple
Derek Ostrander
Senior Project Accountant
PO Box 27 458 Wellington 6571
derek@harrowcollective.example.nz
harrowcollective.example.nz
Full Bleed Size (starting document size) 94 x 58 mm 1110 x 685 pixels * Finished artwork should use the full bleed dimensions for best results. Document Trim Size (final size after being cut) 91 x 55 mm 1075 x 650 pixels * Please be sure to keep all text within the safe margin. Resolution 300 DPI
Simple, perhaps solid colour with the web address (and logo etc)

```html
<!DOCTYPE html>
<html lang="en">
<head>
<meta charset="utf-8">
<title>Harrow Collective – Business Card</title>
<link href="https://fonts.googleapis.com/css2?family=Lato:wght@400;700&display=swap" rel="stylesheet">
<style>
  :root{
    --backdrop:#6e6e6e;
    --brand-blue:#3a86d6;
    --brand-blue-dark:#2a6fb9;
    --card-white:#ffffff;
    --card-grey:#e4e6e9;
    --curve-grey:#b9bcc1;
    --text-dark:#4a4f57;
  }
  html,body{margin:0;padding:0;overflow:hidden;}
  body{
    width:1200px;height:737px;background:var(--backdrop);
    font-family:"Lato",Arial,sans-serif;
    display:flex;align-items:center;justify-content:center;gap:50px;
  }
  .card{
    position:relative;width:530px;height:320px;border-radius:14px;overflow:hidden;
    box-shadow:0 10px 28px rgba(0,0,0,.35);
  }
  .card-front{background:linear-gradient(160deg,var(--card-white) 40%,var(--card-grey) 100%);}
  .card-back{background:var(--brand-blue);display:flex;align-items:center;justify-content:center;}
  .front-curve{position:absolute;inset:0;width:100%;height:100%;}
  .holder{
    position:absolute;top:30px;right:34px;text-align:right;color:#fff;
  }
  .holder-name{font-size:19px;font-weight:700;letter-spacing:2px;text-transform:uppercase;margin:0;}
  .holder-title{font-size:11px;letter-spacing:1px;margin:4px 0 0;opacity:.9;}
  .wordmark{
    display:flex;align-items:center;gap:12px;
    font-weight:700;text-transform:uppercase;letter-spacing:3px;
  }
  .wordmark-dot{width:16px;height:16px;border-radius:50%;flex:none;}
  .card-front .wordmark{position:absolute;left:34px;top:168px;color:var(--brand-blue);font-size:22px;}
  .card-front .wordmark-dot{background:var(--brand-blue);}
  .card-back .wordmark{color:#fff;font-size:26px;}
  .card-back .wordmark-dot{background:#fff;}
  .contact{
    position:absolute;left:34px;bottom:22px;margin:0;padding:0;list-style:none;
    font-size:10.5px;color:var(--text-dark);line-height:17px;
  }
  .contact li{display:flex;align-items:center;gap:8px;}
  .contact svg{width:11px;height:11px;fill:var(--brand-blue);flex:none;}
</style>
</head>
<body>
  <section class="card card-front">
    <svg class="front-curve" viewBox="0 0 530 320" preserveAspectRatio="none" aria-hidden="true">
      <path d="M0,0 H530 V205 C430,120 230,58 0,70 Z" fill="var(--curve-grey)"/>
      <path d="M0,0 H530 V192 C430,108 230,46 0,58 Z" fill="var(--brand-blue)"/>
    </svg>
    <div class="holder">
      <p class="holder-name">Derek Ostrander</p>
      <p class="holder-title">Senior Project Accountant</p>
    </div>
    <div class="wordmark"><span class="wordmark-dot"></span>Harrow Collective</div>
    <ul class="contact">
      <li><svg viewBox="0 0 24 24"><path d="M12 2a7 7 0 0 0-7 7c0 5 7 13 7 13s7-8 7-13a7 7 0 0 0-7-7zm0 9.5A2.5 2.5 0 1 1 12 6.5a2.5 2.5 0 0 1 0 5z"/></svg>PO Box 27 458 Wellington 6571</li>
      <li><svg viewBox="0 0 24 24"><path d="M6.6 10.8a15 15 0 0 0 6.6 6.6l2.2-2.2a1 1 0 0 1 1-.25 11.4 11.4 0 0 0 3.6.57 1 1 0 0 1 1 1V20a1 1 0 0 1-1 1A17 17 0 0 1 3 4a1 1 0 0 1 1-1h3.5a1 1 0 0 1 1 1c0 1.25.2 2.45.57 3.6a1 1 0 0 1-.25 1z"/></svg>Ph 04 555 0187</li>
      <li><svg viewBox="0 0 24 24"><path d="M7 2h10a2 2 0 0 1 2 2v16a2 2 0 0 1-2 2H7a2 2 0 0 1-2-2V4a2 2 0 0 1 2-2zm0 3v13h10V5z"/></svg>Mob 021 555 0142</li>
      <li><svg viewBox="0 0 24 24"><path d="M3 5h18v14H3zm2 2v.5l7 4.5 7-4.5V7z"/></svg>derek@harrowcollective.example.nz</li>
      <li><svg viewBox="0 0 24 24"><path d="M12 2a10 10 0 1 0 0 20 10 10 0 0 0 0-20zm6.9 6h-3a15 15 0 0 0-1.3-3.6A8 8 0 0 1 18.9 8zM12 4a13 13 0 0 1 1.9 4h-3.8A13 13 0 0 1 12 4zM4.3 14a8 8 0 0 1 0-4h3.4a16 16 0 0 0 0 4zm.8 2h3a15 15 0 0 0 1.3 3.6A8 8 0 0 1 5.1 16zm3-8h-3a8 8 0 0 1 4.3-3.6A15 15 0 0 0 8.1 8zM12 20a13 13 0 0 1-1.9-4h3.8A13 13 0 0 1 12 20zm2.3-6H9.7a14 14 0 0 1 0-4h4.6a14 14 0 0 1 0 4zm.3 5.6a15 15 0 0 0 1.3-3.6h3a8 8 0 0 1-4.3 3.6zm1.7-5.6a16 16 0 0 0 0-4h3.4a8 8 0 0 1 0 4z"/></svg>harrowcollective.example.nz</li>
    </ul>
  </section>

  <section class="card card-back">
    <div class="wordmark"><span class="wordmark-dot"></span>Harrow Collective</div>
  </section>
</body>
</html>
```